GUARANTEED WordPress design needed for a sassy, confident charisma coach!

We need a website design for Marla Penrick's brand new, responsive, Wordpress website.
Marla is a trainer / coach who teaches people how to be more charismatic and runs events, publishes video courses and has an ongoing video blog. Her old website is here: www.marlapenrick.co.uk ... but it's now time to have a much better site!
We have a strong idea about the technical components of the website, but we need a designer's eye to create a great style for the site (and provide layered PSD files which our developers will then convert to HTML and CSS).
Marla's brand is sassy, brave, warm and confident. The videos on her existing site give quite a good feel for her personality. We need a clean, stylish and compelling page that isn't too corporate and captures her personality. Every element needs to feel coherent, from fonts and headings to colours and spacing.
The following sites are not exactly what Marla wants (and certainly aren't right in terms of colours) but they give you an idea of the kind of people she is competing against and the area she is operating in:
http://www.tessa-broughley.example/
http://rowanfelsby.example/
Ideally, you will have done something similar and be able to key in on exactly the kind of thing we want: we're not looking to reinvent the wheel. Hopefully you won't mind tweaking a few things if you are close to what we need.
More detail is provided in the word document attached. But in a nutshell we need: a banner, footer, sign-up strap, menu bar, signature and 4 different basic page types. We want bursts of bright colours, contrasted with black and white if possible - sorry we can't be more specific than that...
The word doc also contains some amateur mock-ups as well (the images are also just mockups at this stage) - but although these give a general sense of the structure what we are looking for, we are clearly not designers...so please help! We need a designer's touch!
Kind regards,
Corin
PS The layered PSD versions of the mockup files are available on Cloudvantre: https://files.cloudvantre.example/sh/k72pqa4w1zbtmrd/QXvenlr8Ty3PwMiU6Hs2kYfDb?dl=0
Target Market(s)
Entrepreneurs who need to sell themselves.
Number of Pages Required
4 page

```html
<!DOCTYPE html>
<html lang="en">
<head>
<meta charset="utf-8">
<title>Marla Penrick – Attract, Connect, Influence</title>
<link href="https://fonts.googleapis.com/css2?family=Lato:ital,wght@0,400;0,700;0,900;1,400;1,700&display=swap" rel="stylesheet">
<style>
:root{
  --red:#e2193a;
  --red-soft:#d9475c;
  --ink:#141414;
  --text:#333;
  --muted:#777;
  --line:#dcdcdc;
  --bar:#e6e6e6;
  --yellow:#f7c325;
  --white:#fff;
}
*{box-sizing:border-box;margin:0;padding:0}
html,body{width:1200px;height:2190px;overflow:hidden;background:var(--white)}
body{position:relative;font-family:'Lato',Arial,sans-serif;color:var(--text)}

/* header */
.site-header{position:absolute;left:0;top:0;width:1200px;height:68px;background:var(--white);border-bottom:1px solid #eee}
.brand{position:absolute;left:232px;top:20px;font-family:'Lato',Arial,sans-serif;font-weight:900;font-size:24px;line-height:28px;color:var(--ink);letter-spacing:.5px}
.main-nav{position:absolute;left:562px;top:0;display:flex;height:68px}
.main-nav a{display:block;padding:0 18px;line-height:62px;font-size:12px;font-weight:700;color:var(--ink);text-decoration:none;letter-spacing:.3px}
.main-nav a.is-active{background:var(--red);color:var(--white);position:relative}
.main-nav a.is-active::after{content:"";position:absolute;left:50%;bottom:4px;margin-left:-5px;border:5px solid transparent;border-bottom-color:var(--white)}

/* hero */
.hero{position:absolute;left:0;top:68px;width:1200px;height:348px;background:linear-gradient(115deg,#f7f7f7 0%,#dedede 30%,#f4f4f4 50%,#d8d8d8 75%,#efefef 100%);overflow:hidden}
.hero-title{position:absolute;right:605px;top:90px;text-align:right;font-weight:900;font-size:62px;line-height:74px;color:var(--ink);letter-spacing:2px}
.hero-title .box{display:inline-block;background:var(--red);color:var(--white);padding:0 6px;line-height:64px}
.hero-photo{position:absolute;left:624px;top:0;width:340px;height:348px}
.hero-photo .echo{position:absolute;top:40px;width:110px;height:308px;background:linear-gradient(#d8d8d8 0%,#e6a3ad 40%,#eab5bd 100%);opacity:.6}
.hero-photo .echo.left{left:0}
.hero-photo .echo.right{right:0}
.hero-photo .main{position:absolute;left:100px;top:0;width:140px;height:348px;background:linear-gradient(#cfc9c9 0%,#d44a5d 30%,var(--red) 60%,#c81733 100%)}

/* signup strip */
.signup{position:absolute;left:0;top:416px;width:1200px;height:166px;background:var(--red)}
.signup-foot{position:absolute;left:0;top:582px;width:1200px;height:60px;background:var(--ink)}
.monitor{position:absolute;left:265px;top:420px;width:212px;height:170px}
.monitor .screen{position:absolute;left:0;top:0;width:212px;height:130px;border:6px solid #222;border-radius:4px;background:linear-gradient(135deg,#5a6470,#b8bcc4)}
.monitor .stand{position:absolute;left:86px;top:130px;width:40px;height:28px;background:#c9c9c9}
.monitor .base{position:absolute;left:60px;top:156px;width:92px;height:8px;border-radius:3px;background:#ddd}
.signup-lead{position:absolute;left:505px;top:438px;width:460px;font-style:italic;font-size:16px;line-height:24px;color:var(--white)}
.signup-lead b{font-weight:700}
.field{position:absolute;height:24px;background:var(--white);border-radius:2px;font-size:11px;color:#999;padding:5px 8px}
.field::after{content:"";position:absolute;right:7px;top:8px;width:8px;height:8px;border-radius:50%;background:#bbb}
.btn-yes{position:absolute;height:28px;width:104px;background:var(--yellow);border-radius:2px;font-weight:900;font-size:12px;color:var(--ink);text-align:center;line-height:28px}
.promise{position:absolute;left:504px;top:606px;font-size:11px;color:#ddd}
.socials{position:absolute;display:flex;gap:9px}
.socials span{width:27px;height:27px;border-radius:3px;background:#555;display:block}

/* content */
.bar-title{position:absolute;height:26px;background:linear-gradient(#f1f1f1,var(--bar));border-left:3px solid #bbb;font-size:12px;font-weight:900;color:var(--ink);padding:6px 10px;letter-spacing:.5px}
.post-art{position:absolute;left:225px;width:377px;height:200px;overflow:hidden}
.post-art .art-text{position:absolute;font-weight:900;color:var(--white);text-transform:uppercase}
.art-speaking{background:linear-gradient(135deg,#f36a4c,#e0432f)}
.art-frame{background:linear-gradient(135deg,#3cae4a,#1f8a39)}
.art-style{background:linear-gradient(135deg,#33bde8,#1e9cd0)}
.post-title{position:absolute;left:225px;font-weight:900;font-style:italic;font-size:14px;color:var(--ink)}
.post-meta{position:absolute;left:225px;font-size:9px;color:var(--muted)}
.post-meta b{color:var(--ink);font-style:italic}
.post-excerpt{position:absolute;left:225px;width:377px;font-size:10px;line-height:14px;color:var(--muted)}
.read-more{position:absolute;left:225px;font-size:10px;font-weight:700;color:var(--red)}
.divider{position:absolute;left:225px;width:377px;height:20px}
.divider::before{content:"";position:absolute;left:0;right:0;top:10px;border-top:1px dashed var(--line)}
.divider::after{content:"";position:absolute;left:178px;top:0;width:20px;height:20px;border-radius:50%;background:var(--white);border:1px solid #ccc}

.mini-list{position:absolute;left:617px;top:704px;width:167px}
.mini{display:flex;gap:6px;height:58px;border-bottom:1px solid #eee;padding-top:4px}
.mini .thumb{flex:0 0 68px;height:42px}
.mini p{font-size:9px;font-weight:700;line-height:11px;color:var(--ink)}
.mini small{display:block;font-weight:400;color:var(--muted);font-size:7px;margin-top:3px}

.pager{position:absolute;left:430px;top:1917px;display:flex;gap:6px}
.pager span{width:20px;height:20px;border-radius:50%;border:1px solid #bbb;font-size:10px;line-height:18px;text-align:center;color:var(--muted)}
.pager span.is-current{border-color:var(--red);color:var(--red)}

/* sidebar */
.popular{position:absolute;left:796px;top:700px;width:179px}
.popular li{list-style:none;font-size:10px;line-height:13px;color:var(--text);margin-bottom:12px}
.popular li small{display:block;color:var(--red);font-size:9px;margin-top:3px}
.view-all{position:absolute;left:864px;top:940px;font-size:9px;font-weight:700;color:var(--red)}
.tags{position:absolute;left:796px;top:1003px;width:180px}
.tag-row{display:flex;gap:3px;margin-bottom:3px}
.tags span{background:var(--red);color:var(--white);font-size:9px;padding:3px 4px;line-height:12px;white-space:nowrap}
.tags .t-lg{font-size:16px;line-height:18px;padding:1px 5px}
.tags .t-md{font-size:14px;line-height:16px;padding:1px 5px}
.tags .t-dark{background:var(--ink)}
.promo{position:absolute;left:796px;top:1240px;width:179px;height:385px;background:linear-gradient(#6b6b6b 0%,#3a3a3a 55%,#2a2a2a 100%);color:var(--white)}
.promo-head{position:absolute;left:10px;top:12px;font-weight:900;font-size:17px;line-height:20px}
.promo-live{position:absolute;left:0;top:245px;width:179px;height:52px;background:var(--red);font-weight:900;font-size:40px;text-align:center;line-height:52px}
.promo-places{position:absolute;left:0;top:300px;width:179px;text-align:center;font-style:italic;font-size:16px;font-weight:700}
.promo-places b{color:var(--yellow)}
.promo-btn{position:absolute;left:28px;top:338px;width:122px;height:26px;background:var(--yellow);color:var(--ink);font-weight:900;font-size:12px;text-align:center;line-height:26px}

/* footer */
.newsletter{position:absolute;left:0;top:1973px;width:1200px;height:182px;background:var(--red)}
.newsletter-lead{position:absolute;left:0;top:1996px;width:1200px;text-align:center;font-style:italic;font-size:16px;line-height:27px;color:var(--white)}
.newsletter-note{position:absolute;left:0;top:2113px;width:1200px;text-align:center;font-size:10px;color:#ffd6dc}
.site-footer{position:absolute;left:0;top:2155px;width:1200px;height:35px;background:var(--ink);color:#ccc;font-size:10px}
.site-footer .copy{position:absolute;left:241px;top:12px}
.site-footer nav{position:absolute;left:390px;top:12px;display:flex;gap:22px;font-weight:700;color:var(--white)}
</style>
</head>
<body>

<header class="site-header">
  <div class="brand">Marla Penrick</div>
  <nav class="main-nav">
    <a class="is-active">EVENTS</a><a>WORK WITH ME</a><a>CORPORATE</a><a>ABOUT</a><a>CONTACT</a>
  </nav>
</header>

<section class="hero">
  <h1 class="hero-title"><span class="box">A</span>TTRACT<br>CO<span class="box">N</span>NECT<br>INFLUEN<span class="box">C</span>E</h1>
  <div class="hero-photo" role="img" aria-label="Photo of the coach in a red dress, hands on hips, with faded echoes on either side">
    <div class="echo left"></div>
    <div class="echo right"></div>
    <div class="main"></div>
  </div>
</section>

<section class="signup"></section>
<div class="signup-foot"></div>
<div class="monitor">
  <div class="screen" role="img" aria-label="Video still of the free training shown on a desktop monitor"></div>
  <div class="stand"></div><div class="base"></div>
</div>
<p class="signup-lead">Learn how to unlock the superpower* of your charisma and win all the business you want with this <b>FREE</b> training.</p>
<div class="field" style="left:506px;top:508px;width:177px">First name</div>
<div class="field" style="left:692px;top:508px;width:177px">Email address</div>
<div class="btn-yes" style="left:765px;top:541px">YES PLEASE!</div>
<p class="promise">* Promise to only use your powers for good</p>
<div class="socials" style="left:800px;top:598px"><span></span><span></span><span></span><span></span><span></span></div>

<!-- blog column -->
<div class="bar-title" style="left:225px;top:657px;width:559px">BLOG</div>

<div class="post-art art-speaking" style="top:712px" role="img" aria-label="Blog graphic: coach speaking on stage beside two speech-bubble figures">
  <span class="art-text" style="left:50px;top:90px;font-size:22px">Public speaking...</span>
  <span class="art-text" style="left:95px;top:128px;font-size:20px;text-transform:none">Made Easy :-)</span>
</div>
<h2 class="post-title" style="top:924px">Public speaking...made easy</h2>
<p class="post-meta" style="top:946px">by <b>Pell Arden</b> &nbsp;|&nbsp; July 22, 2016</p>
<p class="post-excerpt" style="top:963px">Lorem ipsum dolor sit amet, consectetur adipiscing elit. Praesent fringilla tortor et mi convallis, ut scelerisque dui rhoncus. Donec quis lorem malesuada, molestie metus id, vehicula lacus. Pellentesque ultricies venenatis ullamcorper. Sed metus ligula, pharetra id risus eu, fermentum auctor eros.</p>
<a class="read-more" style="top:1046px">Read More ➔</a>
<div class="divider" style="top:1074px"></div>

<div class="post-art art-frame" style="top:1130px" role="img" aria-label="Blog graphic: green chalk-style background with the coach smiling">
  <span class="art-text" style="left:18px;top:18px;font-size:18px;line-height:24px">How to start every day<br>in the right frame<br>of mind!</span>
  <span class="art-text" style="left:18px;top:150px;font-size:20px">5 hot tips</span>
</div>
<h2 class="post-title" style="top:1342px">How to start every day in the right frame of mind!</h2>
<p class="post-meta" style="top:1364px">by <b>Pell Arden</b> &nbsp;|&nbsp; July 21, 2016</p>
<p class="post-excerpt" style="top:1381px">Lorem ipsum dolor sit amet, consectetur adipiscing elit. Praesent fringilla tortor et mi convallis, ut scelerisque dui rhoncus. Donec quis lorem malesuada, molestie metus id, vehicula lacus. Pellentesque ultricies venenatis ullamcorper. Sed metus ligula, pharetra id risus eu, fermentum auctor eros.</p>
<a class="read-more" style="top:1464px">Read More ➔</a>
<div class="divider" style="top:1492px"></div>

<div class="post-art art-style" style="top:1546px" role="img" aria-label="Blog graphic: blue background with a red dress sketch and the coach wearing glasses">
  <span class="art-text" style="left:18px;top:20px;font-size:19px;line-height:25px">Take charge<br>of your<br>style...</span>
  <span class="art-text" style="left:18px;top:120px;font-size:19px;line-height:25px">...Boost your<br>confidence</span>
</div>
<h2 class="post-title" style="top:1755px">Take charge of your style...Boost your confidence</h2>
<p class="post-meta" style="top:1777px">by <b>Pell Arden</b> &nbsp;|&nbsp; July 21, 2016</p>
<p class="post-excerpt" style="top:1794px">Lorem ipsum dolor sit amet, consectetur adipiscing elit. Praesent fringilla tortor et mi convallis, ut scelerisque dui rhoncus. Donec quis lorem malesuada, molestie metus id, vehicula lacus. Pellentesque ultricies venenatis ullamcorper. Sed metus ligula, pharetra id risus eu, fermentum auctor eros.</p>
<a class="read-more" style="top:1877px">Read More ➔</a>

<div class="mini-list">
  <div class="mini"><div class="thumb art-style" role="img" aria-label="Style post thumbnail"></div><p>Take charge of your style...<small>July 21, 2016</small></p></div>
  <div class="mini"><div class="thumb" style="background:#e8962e" role="img" aria-label="Unfulfilled post thumbnail"></div><p>Unfulfilled? It's time to think about your...<small>July 20, 2016</small></p></div>
  <div class="mini"><div class="thumb" style="background:#d8402f" role="img" aria-label="Confidence post thumbnail"></div><p>...Boost your confidence<small>July 18, 2016</small></p></div>
  <div class="mini"><div class="thumb art-style" role="img" aria-label="Style post thumbnail"></div><p>Take charge of your style...<small>July 15, 2016</small></p></div>
  <div class="mini"><div class="thumb art-speaking" role="img" aria-label="Public speaking post thumbnail"></div><p>Public speaking... made easy<small>July 12, 2016</small></p></div>
  <div class="mini"><div class="thumb art-frame" role="img" aria-label="Frame of mind post thumbnail"></div><p>How to start every day in the right frame...<small>July 10, 2016</small></p></div>
</div>

<div class="pager">
  <span>‹</span><span class="is-current">1</span><span>2</span><span>3</span><span>4</span><span>›</span>
</div>

<!-- sidebar -->
<div class="bar-title" style="left:796px;top:657px;width:179px">POPULER</div>
<ul class="popular">
  <li>Be more dog: 5 lessons we could learn from our best friends.<small>13/07/15</small></li>
  <li>Are you letting your core beliefs hold you back?<small>08/07/15</small></li>
  <li>How I learned to stop worrying and start NETWORKING!<small>28/06/15</small></li>
  <li>Bitchy resting face and other strange - but true - problems<small>11/06/15</small></li>
</ul>
<a class="view-all">VIEW ALL</a>

<div class="bar-title" style="left:796px;top:968px;width:179px">TAGS</div>
<div class="tags">
  <div class="tag-row" style="padding-left:24px"><span>elip</span><span>body language</span></div>
  <div class="tag-row"><span class="t-lg">capsule wardrobe</span></div>
  <div class="tag-row"><span>confidence</span><span class="t-dark">handshake</span><span>mindset</span></div>
  <div class="tag-row"><span>passion</span><span class="t-lg">power pose</span></div>
  <div class="tag-row"><span>presentations</span><span>presence</span></div>
  <div class="tag-row"><span class="t-md">rapport</span><span>spring wear</span><span>style</span></div>
  <div class="tag-row"><span>values</span><span>vision board</span><span>warmth</span></div>
</div>

<div class="bar-title" style="left:796px;top:1194px;width:179px">COMING UP</div>
<div class="promo" role="img" aria-label="Event banner photo of a live charisma workshop audience">
  <div class="promo-head">UNLOCK<br>THE<br>SUPERPOWER<br>OF<br>CHARISMA</div>
  <div class="promo-live">LIVE</div>
  <div class="promo-places">* Only <b>6</b> places left.</div>
  <div class="promo-btn">LEARN MORE</div>
</div>

<!-- newsletter & footer -->
<section class="newsletter"></section>
<p class="newsletter-lead">Hey! Don't go without signing up because you'll miss out on exclusive offers, awesome tips, and<br>weekly motivation in my fab newsletter *.</p>
<div class="field" style="left:360px;top:2074px;width:177px">First name</div>
<div class="field" style="left:546px;top:2074px;width:177px">Email address</div>
<div class="btn-yes" style="left:733px;top:2072px">YES PLEASE!</div>
<p class="newsletter-note">* And that'll make me sad :-(</p>

<footer class="site-footer">
  <span class="copy">© 2016 Marla Penrick Ltd</span>
  <nav><span>PRIVACY POLICY</span><span>TERMS POLICY</span><span>DISCLAIMERS</span></nav>
  <div class="socials" style="left:800px;top:4px"><span></span><span></span><span></span><span></span><span></span></div>
</footer>

</body>
</html>
```